New Business Cards for Velmora

About Velmora:
At Velmora, we're more than just a company—we're a force for positive change in the staffing industry. Our brand is our heartbeat, and we need a designer who can translate that into every design element.

The Project:
We're revamping our business cards and need your artistic flair to make them stand out. Here's what we're looking for:

- Incorporate our existing brand elements (logo, colours, fonts) into the design.
- Craft a design that's sleek, professional, and memorable.
- Provide options for different layouts and finishes.
- Collaborate closely with our team to ensure the final product exceeds expectations.

Please note: For general text, we use Avenir. The brand guidelines are slightly out of date and don't have correct imaging. Colours are correct though.

```html
<!DOCTYPE html>
<html lang="en">
<head>
<meta charset="utf-8">
<title>Velmora Business Cards</title>
<link rel="stylesheet" href="https://fonts.googleapis.com/css2?family=Montserrat:wght@400;500;600;700&display=swap">
<style>
  :root {
    --backdrop: #3a3a3c;
    --paper: #ffffff;
    --brand-purple: #4e1459;
    --brand-purple-deep: #45104f;
    --brand-purple-light: #5e1f68;
    --brand-magenta: #d4176f;
    --ink: #1e1e24;
    --emboss: #74386f;
  }
  * { box-sizing: border-box; margin: 0; padding: 0; }
  html, body {
    width: 1200px; height: 1200px; overflow: hidden;
    background: var(--backdrop);
    font-family: "Montserrat", sans-serif;
  }
  .canvas { position: relative; width: 1200px; height: 1200px; }
  .card {
    position: absolute; left: 180px; width: 840px; height: 480px;
    border-radius: 30px; overflow: hidden;
  }
  .card--front { top: 70px; background: var(--paper); }
  .card--back {
    top: 650px;
    background: linear-gradient(160deg, var(--brand-purple-light), var(--brand-purple-deep));
  }
  .card__band { position: absolute; inset: 0; width: 100%; height: 100%; }

  .wordmark { position: absolute; color: var(--brand-purple); }
  .wordmark__name { font-weight: 600; line-height: 1; }
  .wordmark__tagline { font-weight: 500; letter-spacing: 1px; text-transform: uppercase; }

  .card--front .wordmark { left: 370px; top: 72px; }
  .card--front .wordmark__name { font-size: 60px; }
  .card--front .wordmark__tagline { font-size: 13px; margin-top: 10px; }

  .contact { position: absolute; left: 120px; top: 250px; color: var(--ink); }
  .contact__name {
    font-size: 36px; font-weight: 700; color: var(--brand-purple);
    letter-spacing: 1px; line-height: 1;
  }
  .contact__title { font-size: 22px; font-weight: 500; margin: 4px 0 10px; letter-spacing: 0.5px; }
  .contact__list { list-style: none; }
  .contact__item {
    display: flex; align-items: center; gap: 12px;
    font-size: 22px; font-weight: 400; line-height: 34px; padding-left: 40px;
  }
  .contact__icon { width: 20px; height: 20px; fill: var(--brand-purple); flex: none; }

  .website {
    position: absolute; right: 48px; bottom: 40px;
    color: var(--paper); font-size: 18px; font-weight: 400; letter-spacing: 0.5px;
  }

  .card--back .wordmark {
    left: 0; right: 0; top: 160px; color: var(--emboss);
    display: flex; flex-direction: column; align-items: center;
  }
  .card--back .wordmark__name { font-size: 110px; }
  .card--back .wordmark__tagline { font-size: 24px; margin-top: 16px; }
</style>
</head>
<body>
<main class="canvas">

  <section class="card card--front" aria-label="Business card front">
    <svg class="card__band" viewBox="0 0 840 480" preserveAspectRatio="none" aria-hidden="true">
      <defs>
        <linearGradient id="stripe" x1="0" x2="1">
          <stop offset="0" stop-color="#d4176f"/>
          <stop offset="0.7" stop-color="#c3177a"/>
          <stop offset="1" stop-color="#6a1a68"/>
        </linearGradient>
      </defs>
      <path d="M0,438 L430,438 C480,438 495,375 560,372 L840,372 L840,400 L560,400 C510,400 490,448 430,448 L0,448 Z" fill="url(#stripe)"/>
      <path d="M0,454 L430,454 C490,454 500,386 565,384 L840,384 L840,480 L0,480 Z" fill="var(--brand-purple)"/>
    </svg>

    <div class="wordmark">
      <div class="wordmark__name">Velmora</div>
      <div class="wordmark__tagline">staffing with purpose</div>
    </div>

    <div class="contact">
      <div class="contact__name">BEN SAMPLE</div>
      <div class="contact__title">TITLE</div>
      <ul class="contact__list">
        <li class="contact__item">
          <svg class="contact__icon" viewBox="0 0 24 24" aria-hidden="true"><path d="M6.6 10.8a15.1 15.1 0 0 0 6.6 6.6l2.2-2.2c.3-.3.7-.4 1-.2 1.1.4 2.3.6 3.6.6.6 0 1 .4 1 1V20c0 .6-.4 1-1 1A17 17 0 0 1 3 4c0-.6.4-1 1-1h3.5c.6 0 1 .4 1 1 0 1.3.2 2.5.6 3.6.1.3 0 .7-.2 1z"/></svg>
          02 5550 1842
        </li>
        <li class="contact__item">
          <svg class="contact__icon" viewBox="0 0 24 24" aria-hidden="true"><path d="M7 1h10a2 2 0 0 1 2 2v18a2 2 0 0 1-2 2H7a2 2 0 0 1-2-2V3a2 2 0 0 1 2-2zm0 3v14h10V4zm5 15.5a1 1 0 1 0 0 2 1 1 0 0 0 0-2z"/></svg>
          0400 555 318
        </li>
        <li class="contact__item">
          <svg class="contact__icon" viewBox="0 0 24 24" aria-hidden="true"><path d="M2 5h20v14H2zm2 2v.5l8 5.5 8-5.5V7zm0 3v7h16v-7l-8 5.5z"/></svg>
          ben@velmora.com.au
        </li>
      </ul>
    </div>

    <div class="website">www.velmora.com.au</div>
  </section>

  <section class="card card--back" aria-label="Business card back">
    <div class="wordmark">
      <div class="wordmark__name">Velmora</div>
      <div class="wordmark__tagline">staffing with purpose</div>
    </div>
  </section>

</main>
</body>
</html>
```